Contemporary new French wine brand needs logo and series of label design

to design a new contemporary logo and series of labels for a new French wine brand. We hope to attract not just current French wine drinkers but new ones who may appreciate a less traditional and more modern style.
Updates

Reason: we are wanting to extend the project for a few days more to receive more submissions since we had fewer designs submitted than we were expecting, maybe because of the holidays.

Target Market(s)

people who follow the arts community (eg. music, theatre, visual/video arts, dance) --- all mature ages.

Industry/Entity Type

French Wine

Requirements
Must have
• a clear, memorable treatment for the name CLAVINE with accompanying logo.
Nice to have
• embossing, matte/gloss refinement, tasteful foil stamping, coated stock for the whites to help the integrity of the paper in and out of ice buckets. A combo of say, three types of fonts; a semi custom font for the brand name Clavine and maybe a script and one other.
Should not have
• not traditional French

```html
<!DOCTYPE html>
<html lang="fr">
<head>
<meta charset="utf-8">
<title>Clavine – Sauvignon Blanc</title>
<link rel="stylesheet" href="https://fonts.googleapis.com/css2?family=Oswald:wght@300;700&family=Great+Vibes&display=swap">
<style>
  :root {
    --label-cream: #e9dcc0;
    --ink: #1b1818;
    --wine-red: #cf3a22;
    --gold: #b8904a;
    --page: #f2f2f0;
  }
  * { margin: 0; padding: 0; box-sizing: border-box; }
  html, body {
    width: 849px;
    height: 1200px;
    overflow: hidden;
    background: var(--page);
  }
  .label {
    position: absolute;
    left: 0;
    top: 0;
    width: 849px;
    height: 1200px;
    background: var(--label-cream);
    display: flex;
    flex-direction: column;
    align-items: center;
  }
  .brand {
    margin-top: 56px;
    display: flex;
    align-items: center;
    gap: 22px;
  }
  .brand-mark {
    width: 34px;
    height: 34px;
    background: var(--gold);
  }
  .brand-name {
    font-family: "Oswald", sans-serif;
    font-weight: 700;
    font-size: 150px;
    line-height: 1;
    letter-spacing: 4px;
    color: var(--ink);
  }
  .artwork {
    margin-top: 36px;
    width: 560px;
    height: 700px;
    background: linear-gradient(90deg, var(--ink) 0%, var(--ink) 48%, var(--wine-red) 52%, var(--wine-red) 78%, var(--ink) 100%);
  }
  .varietal {
    margin-top: 52px;
    font-family: "Oswald", sans-serif;
    font-weight: 300;
    font-size: 64px;
    letter-spacing: 2px;
    color: var(--ink);
    line-height: 1;
  }
  .appellation {
    margin-top: 18px;
    font-family: "Great Vibes", cursive;
    font-size: 52px;
    color: var(--wine-red);
    line-height: 1;
  }
</style>
</head>
<body>
  <main class="label">
    <header class="brand">
      <span class="brand-mark" aria-hidden="true"></span>
      <h1 class="brand-name">CLAVINE</h1>
    </header>
    <div class="artwork" role="img" aria-label="Flat geometric illustration of a dark wine bottle beside a red bottle and a wine glass"></div>
    <p class="varietal">SAUVIGNON BLANC</p>
    <p class="appellation">Val De Loire</p>
  </main>
</body>
</html>
```